Workers comp/Business Ins/ Payroll- Postcard

I own an insurance agency.  I'm interested in getting some professional advice on how to design a message for what i want to sell.  The products I want to sell are 1) Workers compensation 2) business Insurance 3) Payroll processing. They are integrated together but I'm not sure if it's too much to put on a postcard and if I don't put it on a postcard I could be missing out on sales.
I have the ability to look up what Insurance company a business has their workers compensation  policy with, along with their expiration date.  Based on that information I can tell if the business is overpaying for their Workers compensation. insurance. Most companies are overpaying so I can usually save a company money very quickly if I can get in front of them. Some businesses work with a broker such as myself and buy a policy. When it's done this way, the business ESTIMATES his payroll for the year and at the end of the year they have to complete an audit to find out the actual payroll. Based on audit, they will either owe more money if they were low or get money back if they were high. The other way a business buys a workers comp. policy is with their payroll company. The payroll company will place the policy on Pay -as- you -go which means when you pay your employees every week they  will also calculate how much the workers comp premium is for the week and take that amount out of their checking account. This method avoids large down payments, helps with cash flow and should be very accurate at the end of the policy term.  This is by far the best way to do this for the businessowner. My company also has payroll company and we do this for the insured as well. However, most payroll company's such as QVR and Wagemint charge the customer $15 every time they do this so if it's weekly it is another $780 a year.  We also complete the insured's audit for them which is a big headache for the businessowner.
One of our biggest benefits of doing business with our company is we have a  Rate Anchor Forever. When you sign up your base price will never increase. Payroll companies are famous for "discounting a new client" only to increase the rate in a few months later. Our service is also superior to the other payroll companies who use overseas service centers. We have staff within our office and we can answer questions quickly. We usually save businesses money on  their Payroll processing but it's not what we focus on- We focus on the Service.
Business Insurance- One of our main companies that we represent is Tolvan Insurance. Tolvan is very competitive and we usually write business accounts where we save the business owner money but offer superior coverages.
in summary, I'm offering 1) better workers compensation rates 2) Pay as you go workers comp. 3) Rate Anchor, audits done for you, and superior customer service with our payroll company 4) savings on their business insurance with superior coverages.
Sometimes when we talk to an insured we may start with just their payroll and later get the WC and business liability. Each account is different and we do not pressure people to make decisions and we do what is right for them.  The biggest takeaway is we take some things off the plate for the businessowner where they can make just one phone call to get what they need done.  Our Website is www.brackwell-partners.net. my email is tomr@brackwell-partners.net if you have any questions.
Thank You
Tom Rusk

Target Market(s)
Small business owners 1-50 employees
Industry/Entity Type
Insurance and Payroll
Font styles to use
Other font styles liked:
- Let designer choose

Colors
Designer to choose colors to be used in the design.
Requirements
Must have
- It shouldn't be boring- needs to stand out- can use 6x11 inch postcard

Nice to have
- I like humor but not a must

Should not have
- Nothing I can think of

```html
<!DOCTYPE html>
<html lang="en">
<head>
<meta charset="utf-8">
<title>Brackwell Partners Insurance – Postcard</title>
<link rel="stylesheet" href="https://fonts.googleapis.com/css2?family=Archivo:wght@700;800&family=Arimo:wght@400;700&family=Jost:wght@400&family=Poppins:wght@400;600;700&display=swap">
<style>
  :root{
    --page:#2b2c30;
    --panel:#2d2e33;
    --ink:#47484b;
    --red:#8b2527;
    --white:#ffffff;
    --muted:#8a8b8f;
    --photo-light:#6d727d;
    --photo-dark:#3c414c;
    --stamp:#d9d9d9;
    --rule:#3a3d48;
  }
  *{margin:0;padding:0;box-sizing:border-box}
  html,body{width:869px;height:1200px;overflow:hidden;background:var(--page)}
  body{position:relative;font-family:"Arimo",Arial,sans-serif;color:var(--white)}
  .abs{position:absolute;line-height:1;white-space:nowrap}

  /* presentation heading */
  .board-title{position:absolute;left:56px;top:63px;height:51px;border-left:2px solid var(--muted);padding-left:13px;font-family:"Jost",sans-serif;color:var(--muted)}
  .board-title h1{font-weight:400;font-size:31px;line-height:1;margin-top:5px}
  .board-title p{font-size:16px;line-height:1}

  .card{position:absolute;left:78px;width:728px;height:397px;overflow:hidden;box-shadow:0 14px 30px rgba(0,0,0,.45)}
  .card--front{top:184px;background:var(--white)}
  .card--back{top:632px;background:var(--white)}

  /* front */
  .hero-art{position:absolute;left:0;top:0}
  .brand{font-family:"Arimo",sans-serif;font-weight:700;font-size:15px;letter-spacing:.5px;color:var(--red);display:flex;align-items:center;gap:6px}
  .brand__dot{width:9px;height:9px;background:var(--red)}
  .front-brand{left:102px;top:56px}
  .headline{font-family:"Archivo",sans-serif;font-weight:800;font-size:50px;color:var(--ink);letter-spacing:-.5px;left:25px}
  .headline--one{top:87px}
  .headline--two{top:138px}
  .service-tag{display:flex;align-items:center;gap:5px;font-size:11px;color:var(--ink);font-weight:400}
  .service-tag svg{flex:none}
  .band{position:absolute;left:0;top:273px;width:728px;height:124px;background:var(--panel)}
  .band .kicker{left:86px;top:17px;font-family:"Poppins",sans-serif;font-size:10px}
  .band .offer{left:85px;top:27px;font-family:"Poppins",sans-serif;font-weight:700;font-size:30px;line-height:29px;white-space:normal;width:200px}
  .band .fineprint{left:86px;top:91px;font-size:9.5px}
  .band .lock{left:20px;top:24px}
  .band .phone-box{left:427px;top:31px;width:53px;height:53px;background:var(--white);border-radius:4px;display:flex;align-items:center;justify-content:center}
  .band .call{left:497px;top:36px;font-family:"Poppins",sans-serif;font-size:17px;letter-spacing:.5px}
  .band .number{left:496px;top:54px;font-family:"Poppins",sans-serif;font-weight:600;font-size:27px;letter-spacing:1.5px}

  /* back */
  .back-info{position:absolute;left:0;top:0;width:364px;height:397px;background:radial-gradient(ellipse 230px 110px at 190px 0,#8a8a8c 0%,#55565a 45%,var(--panel) 100%)}
  .back-brand{left:236px;top:28px;color:var(--white);font-size:11px}
  .back-brand .brand__dot{background:var(--white);width:7px;height:7px}
  .section-bar{position:absolute;left:0;height:26px;background:var(--red);font-size:16px;font-weight:400;line-height:26px;padding-left:33px}
  .copy{font-size:8px;line-height:13px;color:#e6e6e6}
  .service{position:absolute;left:34px}
  .service h3{display:flex;align-items:center;gap:5px;font-size:13px;font-weight:400;line-height:1}
  .service p{margin-left:22px;margin-top:5px}
  .contact{display:flex;align-items:flex-start;gap:6px;font-size:8px;color:#e6e6e6;line-height:9px}
  .address-side{position:absolute;left:364px;top:0;width:364px;height:397px;background:var(--white)}
  .stamp{position:absolute;left:254px;top:26px;width:69px;height:74px;background:var(--stamp)}
  .rule{position:absolute;left:47px;width:276px;height:1px;background:var(--rule)}
</style>
</head>
<body>

<header class="board-title">
  <h1>Post Card Design</h1>
  <p>Design 1</p>
</header>

<!-- Front of card -->
<section class="card card--front" aria-label="Postcard front">
  <svg class="hero-art" width="728" height="273" viewBox="0 0 728 273">
    <defs>
      <linearGradient id="heroTone" x1="0" y1="0" x2="1" y2="1">
        <stop offset="0" stop-color="var(--photo-light)"/>
        <stop offset="1" stop-color="var(--photo-dark)"/>
      </linearGradient>
    </defs>
    <polygon points="290,0 728,0 728,273 437,273" fill="url(#heroTone)" role="img" aria-label="Photo of a smiling insurance agent in a suit holding a clipboard, with hands offering a small house symbol"/>
    <polygon points="229,273 393,187 437,273" fill="var(--red)"/>
  </svg>

  <div class="abs brand front-brand"><span class="brand__dot"></span>Brackwell Partners</div>

  <div class="abs headline headline--one">INSURANCE</div>
  <div class="abs headline headline--two">AGENCY</div>

  <div class="abs service-tag" style="left:23px;top:191px">
    <svg width="13" height="13" viewBox="0 0 13 13"><circle cx="6.5" cy="6.5" r="6.5" fill="var(--red)"/><path d="M4 6.7l1.8 1.8L9.2 5" stroke="#fff" stroke-width="1.3" fill="none"/></svg>
    Workers compensation
  </div>
  <div class="abs service-tag" style="left:166px;top:191px">
    <svg width="13" height="13" viewBox="0 0 13 13"><circle cx="6.5" cy="6.5" r="6.5" fill="var(--red)"/><circle cx="6.5" cy="6.5" r="3.6" stroke="#fff" stroke-width="1" fill="none"/><text x="6.5" y="8.6" font-size="5.5" text-anchor="middle" fill="#fff" font-family="Arimo,sans-serif">$</text></svg>
    Payroll processing
  </div>
  <div class="abs service-tag" style="left:24px;top:212px">
    <svg width="13" height="13" viewBox="0 0 13 13"><circle cx="6.5" cy="6.5" r="6.5" fill="var(--red)"/><path d="M4 6l2.5-2.2L9 6v3.2H4z" stroke="#fff" stroke-width="1" fill="none"/></svg>
    Business Insurance
  </div>

  <div class="band">
    <svg class="abs lock" width="50" height="72" viewBox="0 0 50 72" aria-hidden="true">
      <path d="M11 30V17a14 14 0 0 1 28 0v13" stroke="#fff" stroke-width="6" fill="none"/>
      <circle cx="25" cy="47" r="24" fill="#fff"/>
      <circle cx="25" cy="47" r="16" fill="var(--panel)"/>
      <text x="25" y="55" font-size="22" font-weight="700" text-anchor="middle" fill="#fff" font-family="Poppins,sans-serif">$</text>
    </svg>
    <div class="abs kicker">One of our biggest benefits</div>
    <div class="abs offer">Rate Anchor Forever</div>
    <div class="abs fineprint">When you sign up your base price will never increase</div>

    <div class="abs phone-box">
      <svg width="34" height="34" viewBox="0 0 24 24" aria-hidden="true">
        <path d="M6.6 3.5l2.3 3.2-1.6 2a11 11 0 0 0 6 6l2-1.6 3.2 2.3-1.2 3A2 2 0 0 1 15 19.5 15 15 0 0 1 4.5 9 2 2 0 0 1 5.6 6.7z" fill="none" stroke="var(--panel)" stroke-width="1.4" stroke-linejoin="round"/>
        <path d="M14 3.5a6.5 6.5 0 0 1 6.5 6.5M14 6.5a3.5 3.5 0 0 1 3.5 3.5" fill="none" stroke="var(--panel)" stroke-width="1.4" stroke-linecap="round"/>
      </svg>
    </div>
    <div class="abs call">Call to fine out more</div>
    <div class="abs number">+1-555-0188</div>
  </div>
</section>

<!-- Back of card -->
<section class="card card--back" aria-label="Postcard back">
  <div class="back-info">
    <div class="abs brand back-brand"><span class="brand__dot"></span>Brackwell Partners</div>

    <h2 class="section-bar" style="top:45px;width:202px">About Our Company</h2>
    <p class="abs copy" style="left:36px;top:74px;white-space:normal;width:300px">Lorem ipsum dolor sit amet consectetur adipiscing elit. Quisque faucibus ex sapien vitae pellentesque sem placerat. In id cursus mi pretium tellus duis convallis. Tempus leo eu aenean sed diam urna tempor.</p>

    <h2 class="section-bar" style="top:120px;width:155px;height:24px;line-height:24px">Our Services</h2>

    <div class="service" style="top:148px">
      <h3><svg width="15" height="15" viewBox="0 0 15 15"><circle cx="7.5" cy="7.5" r="7.5" fill="#fff"/><circle cx="7.5" cy="7.5" r="4.5" stroke="var(--red)" fill="none"/><path d="M5.5 7.6l1.4 1.4 2.6-2.6" stroke="var(--red)" fill="none"/></svg>Workers compensation</h3>
      <p class="copy">Lorem ipsum dolor sit amet consectetur adipiscing elit.<br>Quisque faucibus ex sapien vitae.</p>
    </div>
    <div class="service" style="top:197px">
      <h3><svg width="15" height="15" viewBox="0 0 15 15"><circle cx="7.5" cy="7.5" r="7.5" fill="#fff"/><path d="M4.5 7.2l3-2.6 3 2.6v3.3h-6z" fill="var(--red)"/></svg>Business Insurance</h3>
      <p class="copy">Lorem ipsum dolor sit amet consectetur adipiscing elit.<br>Quisque faucibus ex sapien vitae.</p>
    </div>
    <div class="service" style="top:243px">
      <h3><svg width="15" height="15" viewBox="0 0 15 15"><circle cx="7.5" cy="7.5" r="7.5" fill="#fff"/><circle cx="7.5" cy="7.5" r="4" stroke="var(--red)" fill="none"/><text x="7.5" y="9.8" font-size="6" text-anchor="middle" fill="var(--red)" font-family="Arimo,sans-serif">$</text></svg>Payroll processing</h3>
      <p class="copy">Lorem ipsum dolor sit amet consectetur adipiscing elit.<br>Quisque faucibus ex sapien vitae.</p>
    </div>

    <h2 class="section-bar" style="top:294px;width:155px;height:29px;line-height:29px;font-size:18px">Contact</h2>

    <div class="abs contact" style="left:34px;top:330px">
      <svg width="11" height="13" viewBox="0 0 11 13"><path d="M5.5 12S1 7.5 1 5a4.5 4.5 0 0 1 9 0c0 2.5-4.5 7-4.5 7z" fill="none" stroke="#fff"/><circle cx="5.5" cy="5" r="1.5" fill="none" stroke="#fff"/></svg>
      <span>Your Address Goes Here, 999 City,<br>Country.</span>
    </div>
    <div class="abs contact" style="left:34px;top:352px">
      <svg width="13" height="13" viewBox="0 0 24 24"><path d="M6.6 3.5l2.3 3.2-1.6 2a11 11 0 0 0 6 6l2-1.6 3.2 2.3-1.2 3A2 2 0 0 1 15 19.5 15 15 0 0 1 4.5 9 2 2 0 0 1 5.6 6.7z" fill="none" stroke="#fff" stroke-width="1.8"/></svg>
      <span style="padding-top:2px">+1-555-0188</span>
    </div>
    <div class="abs contact" style="left:206px;top:329px">
      <svg width="14" height="11" viewBox="0 0 14 11"><rect x=".5" y=".5" width="13" height="10" fill="none" stroke="#fff"/><path d="M.5 .5L7 6l6.5-5.5" fill="none" stroke="#fff"/></svg>
      <span style="padding-top:1px">tomr@brackwell-partners.net</span>
    </div>
    <div class="abs contact" style="left:206px;top:351px">
      <svg width="13" height="13" viewBox="0 0 14 14"><circle cx="7" cy="7" r="6.3" fill="none" stroke="#fff"/><ellipse cx="7" cy="7" rx="2.8" ry="6.3" fill="none" stroke="#fff"/><path d="M.7 7h12.6M1.8 3.8h10.4M1.8 10.2h10.4" stroke="#fff" stroke-width=".8"/></svg>
      <span style="padding-top:2px">www.brackwell-partners.net</span>
    </div>
  </div>

  <div class="address-side">
    <div class="stamp"></div>
    <div class="rule" style="top:213px"></div>
    <div class="rule" style="top:243px"></div>
    <div class="rule" style="top:273px"></div>
    <div class="rule" style="top:303px"></div>
    <div class="rule" style="top:332px"></div>
  </div>
</section>

</body>
</html>
```